Design door hanger Bonaire Diving

We would like to have a design for a door hanger (See example below).
One side: Promote reef taster diving.
Other side: Promote Unlimited air/nitrox packages - lowest price guaranteed on Bonaire

We would like to inform people who rent a car with us about our air packages for diving. And non divers should be triggered to come and do a Reef Taster Dive with us. (KT Car rental and KT Dive is the same company.)

Target Market(s)

Divers and potential divers

Industry/Entity Type

Diving industry

Font styles to use
Sans Serif

Colors
0054AA
0677BA
7BADD7
CADEEF
E8F1F8
EE7325
F08F49
F5BC92
FAE3D3
FDF4ED

Requirements
Must have
• a few of the pictures included

```html
<!DOCTYPE html>
<html lang="en">
<head>
<meta charset="utf-8">
<title>KT Dive – Door Hangers</title>
<link href="https://fonts.googleapis.com/css2?family=Montserrat:ital,wght@0,700;0,800;1,800&family=Open+Sans:ital,wght@1,400;1,600;1,700&display=swap" rel="stylesheet">
<style>
  :root{
    --night:#01233a;
    --orange:#f6aa2b;
    --navy:#1f2b57;
    --sky:#a6d9f3;
    --white:#ffffff;
    --deep:#4f78ad;
  }
  *{margin:0;padding:0;box-sizing:border-box}
  html,body{width:1200px;height:1200px;overflow:hidden;background:var(--night)}
  .canvas{position:relative;width:1200px;height:1200px}
  .shapes{position:absolute;left:0;top:0;width:1200px;height:1200px}
  .side{position:absolute;top:0;width:403px;height:1200px;text-align:center;color:var(--navy)}
  .side--taster{left:161px}
  .side--air{left:636px}
  .brand{position:absolute;left:0;right:0;top:452px;font-family:"Montserrat",sans-serif;font-weight:800;font-size:38px;line-height:40px;color:var(--navy);letter-spacing:.5px}
  .headline{position:absolute;left:0;right:0;font-family:"Montserrat",sans-serif;font-weight:800;color:var(--navy)}
  .headline .accent{color:var(--orange)}
  .side--taster .headline{top:586px;font-size:25px;text-shadow:0 0 6px rgba(255,255,255,.9)}
  .side--air .headline{top:590px;font-size:20.5px;line-height:28px}
  .intro{position:absolute;left:0;right:0;font-family:"Open Sans",sans-serif;font-style:italic;font-weight:400;color:var(--navy)}
  .side--taster .intro{top:626px;font-size:16.5px;line-height:21.5px}
  .side--air .intro{top:652px;font-size:15.5px;line-height:21px}
  .intro strong{font-weight:700}
  .gift{position:absolute;left:0;right:0;top:700px;font-family:"Montserrat",sans-serif;font-weight:700;font-size:19px;color:var(--navy);text-shadow:0 0 5px rgba(255,255,255,.9)}
  .gift .accent{color:var(--orange);font-family:"Open Sans",sans-serif;font-style:italic;font-weight:600}
  .facts{position:absolute;left:28px;right:20px;top:744px;list-style:none;text-align:left;font-family:"Open Sans",sans-serif;font-style:italic;font-size:12.4px;line-height:16px;color:var(--white)}
  .facts li::before{content:"• "}
  .contact{position:absolute;left:0;right:0;top:1122px;font-family:"Open Sans",sans-serif;font-style:italic;font-weight:700;font-size:18px;color:var(--navy);word-spacing:2px}
  .contact span+span{margin-left:16px}
</style>
</head>
<body>
<div class="canvas">
  <svg class="shapes" viewBox="0 0 1932 1932" xmlns="http://www.w3.org/2000/svg">
    <defs>
      <path id="hanger-outline" d="M260,396 A324,324 0 0 1 908,396 L908,1820 Q908,1860 868,1860 L300,1860 Q260,1860 260,1820 L260,760 Q261,732 287,716 L646,517 A132,132 0 1 0 452,400 A96,96 0 0 1 260,396 Z"/>
      <clipPath id="hanger-clip"><use href="#hanger-outline"/></clipPath>
      <linearGradient id="taster-body" x1="0" y1="0" x2="0" y2="1">
        <stop offset="0" stop-color="#ffffff"/>
        <stop offset=".28" stop-color="#d9ecf8"/>
        <stop offset=".5" stop-color="#8dbde3"/>
        <stop offset=".75" stop-color="#5f86bb"/>
        <stop offset="1" stop-color="#4a6fa6"/>
      </linearGradient>
      <linearGradient id="reef-photo" x1="0" y1="0" x2="0" y2="1">
        <stop offset="0" stop-color="#5476a8" stop-opacity="0"/>
        <stop offset=".2" stop-color="#3f7990"/>
        <stop offset=".6" stop-color="#2f6a72"/>
        <stop offset="1" stop-color="#3f5a5c"/>
      </linearGradient>
      <linearGradient id="air-body" x1="0" y1="0" x2="0" y2="1">
        <stop offset="0" stop-color="#ffffff"/>
        <stop offset=".3" stop-color="#ffffff"/>
        <stop offset=".45" stop-color="#d3edf3"/>
        <stop offset=".6" stop-color="#6cbcd6"/>
        <stop offset=".72" stop-color="#1f88c2"/>
        <stop offset=".82" stop-color="#8ec9dc"/>
        <stop offset=".9" stop-color="#c8d9d6"/>
        <stop offset="1" stop-color="#6a6a5e"/>
      </linearGradient>
    </defs>

    <g class="hanger hanger--taster" clip-path="url(#hanger-clip)">
      <rect x="250" y="60" width="670" height="1810" fill="var(--orange)"/>
      <path d="M260,700 C450,590 700,540 908,535 L908,610 C650,612 420,680 260,760 Z" fill="var(--sky)"/>
      <path d="M260,760 C420,680 650,612 908,610 L908,1800 L260,1800 Z" fill="url(#taster-body)"/>
      <rect x="260" y="1330" width="648" height="470" fill="url(#reef-photo)" role="img" aria-label="Photo of a coral reef with fish, a parrotfish and a seahorse"/>
      <path d="M260,1700 C480,1790 720,1790 908,1720 L908,1870 L260,1870 Z" fill="var(--sky)"/>
      <path d="M260,1690 C420,1760 600,1770 720,1770 C800,1770 860,1780 908,1800 L908,1870 L260,1870 Z" fill="var(--orange)" transform="translate(0,20)"/>
    </g>

    <g class="hanger hanger--air" transform="translate(765,0)">
      <g clip-path="url(#hanger-clip)">
        <rect x="250" y="60" width="670" height="1810" fill="var(--orange)"/>
        <path d="M260,540 C450,520 700,520 908,535 L908,610 C650,612 420,620 260,605 Z" fill="var(--sky)"/>
        <path d="M260,605 C420,620 650,612 908,610 L908,1800 L260,1800 Z" fill="#ffffff"/>
        <rect x="260" y="1000" width="648" height="800" fill="url(#air-body)" role="img" aria-label="Photo of a sea turtle swimming over sand and two scuba tanks with regulators on a rock"/>
        <path d="M260,1760 C480,1730 720,1700 908,1680 L908,1870 L260,1870 Z" fill="var(--sky)"/>
        <path d="M260,1790 C480,1770 720,1740 908,1730 L908,1870 L260,1870 Z" fill="var(--orange)"/>
      </g>
    </g>
  </svg>

  <section class="side side--taster">
    <div class="brand">KT Car rental<br>&amp; Dive</div>
    <h2 class="headline">Reef Taster <span class="accent">Diving</span></h2>
    <p class="intro">Dive for the first time and enjoy our<br>underwater paradise to the fullest<br>under the guidance of an instructor.</p>
    <p class="gift">Give <span class="accent">yourself a lifetime</span> gift.</p>
    <ul class="facts">
      <li>Ages 10 and up can sign up for our taster dive.</li>
      <li>The Reef Taster Diving course will take 3-4 hours.</li>
      <li>A group consists of a maximum of 4 people</li>
      <li>Experience the splendor of the ocean without much distraction by other divers.</li>
      <li>Enjoy a lot of personal attention given by your instructor.</li>
    </ul>
    <p class="contact"><span>kt-dive.com</span><span>+599 700 4512</span></p>
  </section>

  <section class="side side--air">
    <div class="brand">KT Car rental<br>&amp; Dive</div>
    <h2 class="headline">Unlimited <span class="accent">sustainable air<br>at a competitive rate</span></h2>
    <p class="intro">KT-Dive offers unlimited air/nitrox for the<br><strong>lowest price</strong> on Bonaire.<br>We fill your tank up to 3200 PSI<br><strong>(220 BAR)</strong> without problem.</p>
    <p class="contact"><span>kt-dive.com</span><span>+599 700 4512</span></p>
  </section>
</div>
</body>
</html>
```